Website Makeover for Local small business Law Enforcement Vendor

We are a very small business (2-3 employees) that provides training and study products to police officers study for promotion exams, as well as other law enforcement training. We currently use NestHarbor as our hosting company and we use one of there template makers for our web design. So your design will have to be compatible and easy for a novice to upload in place of the current NestHarbor template. This is vital. You will need to provide detailed instructions on how to convert your design to our existing website.

The website has an accompanying web store were customers can buy products, ultimately we'd like a full integration between the main website and the on-line store. However, we can't afford to have our site or store down for any period of time.

Our web address is www.trelvanrankprep.us It is simple and unprofessional. We'd like it to be modern and inviting.

We have four main categories of services/products:

1. Police Promotion Exam Preparation
2. Police Training
3. Police Entrance Exam Services
4. Police Department Services

We are open to your expertise and suggestions. We don't have many photos/graphics to offer you.
Updates

Target Market(s)

Police officers and Police Departments

Industry/Entity Type

Small Business

Requirements
Must have
• Easy conversion to existing NestHarbor hosting - with detailed instructions.

Link to our webstore - unless you can better integrate to existing site.

The ability for a novice to modify content and load updates with ease.
Nice to have
• The ability to post PDF's and/or Word documents for download by others (registration forms etc.)

```html
<!DOCTYPE html>
<html lang="en">
<head>
<meta charset="utf-8">
<title>Trelvan Consulting, LLC</title>
<link rel="stylesheet" href="https://fonts.googleapis.com/css2?family=Oswald:wght@500;600&family=Exo+2:ital,wght@1,800&family=Arimo:wght@400;700&display=swap">
<style>
:root{
  --navy:#0f1f6a;
  --navy-deep:#071142;
  --footer:#080f3a;
  --yellow:#fcc61c;
  --nav-blue:#4a79d6;
  --grey:#efefef;
  --card:#f6f6f6;
  --ink:#222;
  --white:#fff;
}
*{box-sizing:border-box;margin:0;padding:0}
html,body{width:910px;height:1200px;overflow:hidden}
body{position:relative;background:var(--white);font-family:Arimo,Arial,sans-serif;color:var(--ink)}
.header{position:absolute;left:0;top:0;width:910px;height:58px;background:var(--white)}
.brand{position:absolute;left:28px;top:12px;display:flex;align-items:center;gap:10px}
.brand-dot{width:34px;height:34px;border-radius:50%;background:var(--yellow)}
.brand-name{font-family:"Exo 2",sans-serif;font-style:italic;font-weight:800;font-size:24px;color:var(--navy);letter-spacing:.5px}
.phone{position:absolute;left:545px;top:18px;display:flex;align-items:center;gap:6px;font-size:23px;color:#222}
.email{position:absolute;right:24px;top:35px;font-size:11px;color:#555}
.topline{position:absolute;left:0;top:58px;width:910px;height:40px;background:var(--navy-deep)}
.nav{position:absolute;left:17px;top:64px;width:874px;height:35px;background:var(--yellow);display:flex;align-items:center}
.nav a{font-family:Oswald,sans-serif;font-weight:600;font-size:16px;color:var(--navy);text-decoration:none;padding:0 17px;height:35px;line-height:35px}
.nav a.active{background:var(--nav-blue);color:var(--white);padding:0 16px;margin-left:104px}
.hero{position:absolute;left:0;top:98px;width:910px;height:331px;background:linear-gradient(90deg,#1c1a1c 0%,#3b342f 40%,#6a6260 70%,#2a2e3c 100%)}
.hero-title{position:absolute;left:21px;top:150px;font-family:"Exo 2",sans-serif;font-style:italic;font-weight:800;font-size:31px;color:#ddd;letter-spacing:.5px}
.hero-sub{position:absolute;left:21px;top:189px;font-size:16px;color:#eee;letter-spacing:.3px}
.hero-note{position:absolute;left:21px;top:226px;font-size:11.5px;line-height:13px;color:#eee}
.hero-note span{color:var(--yellow)}
.cta{position:absolute;left:18px;top:289px;width:339px;height:36px;background:var(--yellow);border-bottom:4px solid #b88a0c;font-family:"Exo 2",sans-serif;font-style:italic;font-weight:800;font-size:16px;color:var(--navy);line-height:34px;text-align:center}
.content{position:absolute;left:17px;top:365px;width:876px;height:714px;background:var(--grey)}
.cats{position:absolute;left:17px;top:365px;width:876px;height:154px;background:var(--card);border-top:6px solid var(--yellow);display:flex}
.cat{flex:1;border-right:1px solid #d8d8d8;text-align:center;padding-top:15px}
.cat:last-child{border:none}
.cat-img{width:86px;height:88px;margin:0 auto;border:1px solid #ddd}
.cat-label{font-family:Oswald,sans-serif;font-weight:500;font-size:13px;line-height:15px;color:#222;margin-top:8px;text-transform:uppercase}
.service{position:absolute;width:414px;height:143px;background:var(--navy);display:flex;padding:12px 12px}
.service-img{width:149px;height:119px;flex:none;border:1px solid #31428f}
.service-body{padding:1px 0 0 19px}
.service h3{font-family:"Exo 2",sans-serif;font-style:italic;font-weight:800;font-size:16px;line-height:20px;color:#c9d1ef;text-transform:uppercase;letter-spacing:.3px}
.service p{font-size:11.5px;line-height:13.5px;color:#c9d1ef;margin-top:6px}
.service .more{display:block;margin-top:8px;font-size:11.5px;color:var(--yellow)}
.testi-head{position:absolute;left:34px;top:868px;font-family:"Exo 2",sans-serif;font-style:italic;font-weight:800;font-size:22px;color:#333}
.more-stories{position:absolute;right:38px;top:879px;font-size:13px;font-weight:700;color:var(--navy);display:flex;align-items:center;gap:7px}
.bubble{position:absolute;top:916px;width:257px;height:133px;background:var(--yellow);border-radius:9px;padding:0 22px;display:flex;align-items:center;font-size:11.2px;line-height:13.4px;color:#1c1c3a}
.bubble::after{content:"";position:absolute;left:48px;bottom:-16px;border-right:16px solid transparent;border-top:17px solid var(--yellow)}
.footer{position:absolute;left:0;top:1079px;width:910px;height:121px;background:var(--footer)}
.foot-links{position:absolute;left:23px;top:40px;font-size:12px;color:var(--white);display:flex;gap:9px}
.copy{position:absolute;left:22px;top:60px;font-size:10px;color:#dde}
.foot-brand{position:absolute;left:684px;top:36px;width:56px;height:56px;border-radius:50%;background:#2a3478}
.foot-addr{position:absolute;left:754px;top:40px;font-size:10.5px;font-weight:700;line-height:13px;color:var(--white)}
</style>
</head>
<body>
<header class="header">
  <div class="brand"><span class="brand-dot"></span><span class="brand-name">TRELVAN CONSULTING, LLC</span></div>
  <div class="phone">
    <svg width="28" height="28" viewBox="0 0 28 28" aria-hidden="true"><circle cx="14" cy="14" r="12.5" fill="none" stroke="#222" stroke-width="2"/><path d="M9.5 7.5l3 3-1.6 1.9c.9 2 2.4 3.5 4.2 4.3l1.9-1.6 3 3-1.8 2.2c-5-.7-9.2-4.8-10.1-10z" fill="#222"/></svg>
    555.014.2738
  </div>
  <div class="email">sales@trelvanrankprep.us</div>
</header>
<div class="topline"></div>
<div class="hero" role="img" aria-label="Smiling police officer standing in front of a patrol car with lights on at dusk"></div>
<nav class="nav">
  <a class="active">HOME</a><a>ABOUT US</a><a>FREE RESOURCES</a><a>PROMOTIONS</a><a>EMPLOYMENT</a><a>DEPARTMENT SERVICES</a>
</nav>
<h1 class="hero-title">TRELVAN CONSULTING, LLC</h1>
<p class="hero-sub">POLICE PROMOTIONS, TRAINING, SELECTION &amp; MORE</p>
<p class="hero-note">FOR FREE Corvale Exam Practice Questions -<br>Send an email to <span>questions@trelvanrankprep.us</span> and type in CORVALE.</p>
<div class="cta">CHECK UPCOMING COURSE SCHEDULE</div>

<div class="content"></div>
<section class="cats">
  <div class="cat"><div class="cat-img" style="background:#e7e2d6" role="img" aria-label="Department badge"></div><div class="cat-label">Harwick<br>Police Products</div></div>
  <div class="cat"><div class="cat-img" style="background:#d9d6cf" role="img" aria-label="Department badge"></div><div class="cat-label">Corvale<br>Sergeant Exam</div></div>
  <div class="cat"><div class="cat-img" style="background:linear-gradient(#6d7fa0,#2b3350)" role="img" aria-label="Officers at a promotion ceremony"></div><div class="cat-label">Police<br>Promotions</div></div>
  <div class="cat"><div class="cat-img" style="background:linear-gradient(#7fa4d8,#3c3f4a)" role="img" aria-label="Officer making an arrest during training"></div><div class="cat-label">Police Training<br>&amp; References</div></div>
</section>

<article class="service" style="left:31px;top:533px">
  <div class="service-img" style="background:linear-gradient(135deg,#c48a4a,#1d2440)" role="img" aria-label="Row of uniformed officers at a ceremony"></div>
  <div class="service-body"><h3>Police Promotional<br>Preparation</h3><p>We have quickly become the leader in Police Promotional Preparation in Massachusetts.</p><span class="more">read more +</span></div>
</article>
<article class="service" style="left:462px;top:533px">
  <div class="service-img" style="background:linear-gradient(135deg,#5a4a48,#1a1c2c)" role="img" aria-label="Recruits in uniform during inspection"></div>
  <div class="service-body"><h3>Police Employment<br>Preparation</h3><p>Exam preparation, interviewing &amp; assessment centers, career path and job search</p><span class="more">read more +</span></div>
</article>
<article class="service" style="left:31px;top:691px">
  <div class="service-img" style="background:linear-gradient(135deg,#8d96a8,#2a2f3c)" role="img" aria-label="Officers seated in a training classroom"></div>
  <div class="service-body"><h3>Police Training &amp;<br>Education</h3><p>Advanced &amp; Specialized legal training for State, Municipal and Campus Police. Custom tailor training to the needs.</p><span class="more">read more +</span></div>
</article>
<article class="service" style="left:462px;top:691px">
  <div class="service-img" style="background:linear-gradient(135deg,#c4cad2,#3a3e48)" role="img" aria-label="Officer writing a ticket beside a car"></div>
  <div class="service-body"><h3>Law Enforcement<br>Agency Services</h3><p>Training, Entrance and Promotional Exam creation and administration, Assessment Centers and selection assistance.</p><span class="more">read more +</span></div>
</article>

<h2 class="testi-head">TESTIMONIALS FROM PREVIOUS CLIENTS</h2>
<div class="more-stories"><svg width="8" height="10" viewBox="0 0 8 10" aria-hidden="true"><path d="M0 0l8 5-8 5z" fill="#0f1f6a"/></svg>MORE SUCCESS STORIES</div>

<blockquote class="bubble" style="left:32px">Hey Daniel, I just wanted to let you know that I was lucky enough to get promoted to Chief last week here in XXXXX. Part of the reason I was able to do that was because of you. I am not sending this for any other reason but to say thanks and if there is ever anything I can do to help you in the future please feel free to call.</blockquote>
<blockquote class="bubble" style="left:325px">Hi Daniel, I followed the personal trainer religiously every week, utilized study guides, edge outlines, and flashcards...One of only two in (a large agency) who passed the LT. exam. No question about it the program works, without program I would not be number one on LT. exam. Thank you again.</blockquote>
<blockquote class="bubble" style="left:618px">Daniel- I scored a 78! At first I was glad I passed but thought I had done so much better. Then I found out that only one other person in my department passed and he got a 74 (7 out of 9 failed). So I'm allegedly at the top. The difference was undoubtedly the edge and seminars. Thanks again.</blockquote>

<footer class="footer">
  <div class="foot-links"><span>Home</span><span>About Us</span><span>Free Resources</span><span>Promotions</span><span>Employment</span><span>Department</span></div>
  <div class="copy">Copyright 2014. Trelvan Consulting. All rights reserved.</div>
  <div class="foot-brand"></div>
  <div class="foot-addr">Trelvan Consulting, LLC<br>P.O. Box 418<br>Millbrook, MA 01990<br>(555) 014-2738<br>Fax (555) 014-2790</div>
</footer>
</body>
</html>
```